Large online photo magazine needs redesign

We have previously digitised a historical photographic magazine of around 20,000 printed pages and made it available online. The magazine ran up to the early 1970s, and the content is largely black and white photographs of local events, accompanied by short captions.

Although the content is very rich, the design needs to be revisited so that:
* it is visually appealing
* it is responsive (i.e. works in browsers across all manner of devices)
* is faithful to the nature of the content

There are only a few core page types, and the central one is the article page, an example of which can be seen at:
http://lanternweekly.org.nz/gisborne/issue/KLW81_19600714/t1-body-d4.html

Any design submitted should be based on the treatment of an article page such as the above.

Given the large number of pages on our site, we need a design which can be templated to work for any content in the collection, i.e. we cannot hand-craft our templates to match a given page of content, rather a template must work acceptably well for all content.

The current site, although basic in design, has the advantage that it is quite efficient in the amount of data per page request (around 100k - 200k). While not adverse to web fonts, banner imagery etc, we will carefully consider the benefit gained from any such treatment against the amount of extra data that needs to be downloaded to the client's browser.

For the right design, we are able ourselves to adapt it to a CSS layout.

An example of each core page type is as follows (though for this project we only expect a design for a single page, as itemised above):

http://lanternweekly.org.nz/gisborne/index.html
http://lanternweekly.org.nz/gisborne/about.html
http://lanternweekly.org.nz/gisborne/help.html
http://lanternweekly.org.nz/gisborne/initial/index.html
http://lanternweekly.org.nz/gisborne/search/results?type=section&text=smith&cmdSubmit=Go
http://lanternweekly.org.nz/gisborne/advanced-search/index.html
http://lanternweekly.org.nz/gisborne/issue/KLW81_19600714/t1-front-d1.html
http://lanternweekly.org.nz/gisborne/issue/KLW81_19600714/index.html
http://lanternweekly.org.nz/gisborne/issue/KLW81_19600714/fig-KLW81_19600714_005a.html
http://lanternweekly.org.nz/gisborne/issue/KLW81_19600714/KLW81_19600714_012.html
http://lanternweekly.org.nz/gisborne/issue/KLW81_19600714/thumbnails.html

Target Market(s)

A general browsing audience of all ages, but skewed towards the older generations, and those interested in family / regional history.

The average user will not be particularly web-savy, and the treatment of the content should not detract / distract from the actual content itself.

Industry/Entity Type

Events

Requirements
Must have
• * it is visually appealing
The content should be visually appealing to the audience, which can be defined as a general browsing audience of all ages, but skewed towards the middle and older generations.

* it is responsive (the design can be adapted - by us - to work in browsers across all manner of devices)

The magazine covers (http://lanternweekly.org.nz/gisborne/issues/index.html) offer some possible inspiration for treatment of the material.

```html
<!DOCTYPE html>
<html lang="en">
<head>
<meta charset="utf-8">
<title>Lantern Weekly — Home</title>
<link href="https://fonts.googleapis.com/css2?family=Arimo:wght@400;700&family=Gelasio:wght@400;700&family=Tinos:wght@400;700&display=swap" rel="stylesheet">
<style>
:root{
  --brand-red:#c9384d;
  --accent-red:#d1333c;
  --nav-dark:#2f2f2f;
  --footer-dark:#333333;
  --ink:#111111;
  --link-blue:#1a1aff;
  --rule:#222222;
  --paper:#ffffff;
  --page-tone:#d9d8d2;
}
*{box-sizing:border-box;margin:0;padding:0}
html,body{width:1200px;height:2750px;overflow:hidden;background:var(--paper)}
body{font-family:"Arimo",Arial,sans-serif;color:var(--ink);position:relative}
a{color:var(--link-blue)}

.search-bar{height:50px;position:relative}
.search-bar .field{position:absolute;left:724px;top:8px;width:254px;height:34px;border:2px solid #555}
.search-bar .go{position:absolute;left:986px;top:6px;width:40px;height:38px;background:#2b2b2b;border-radius:3px}
.search-bar .advanced{position:absolute;left:1036px;top:8px;font-family:"Tinos",serif;font-size:23px}

.masthead{height:104px;background:var(--brand-red);display:flex;align-items:center;padding-left:58px}
.masthead .brand{font-family:"Gelasio",serif;font-weight:700;font-size:84px;line-height:1;color:#fff;letter-spacing:4px}

.main-nav{height:48px;background:var(--nav-dark);position:relative}
.main-nav a{position:absolute;top:12px;color:#fff;text-decoration:none;font-size:21px}
.main-nav a.current{color:var(--accent-red);text-decoration:underline}

.spread{position:absolute;left:98px;top:224px;width:978px;height:628px;background:var(--page-tone);border:1px solid #999}
.spread .panel{position:absolute}
.spread .gutter{position:absolute;left:488px;top:0;width:6px;height:100%;background:linear-gradient(90deg,#b5b4ae,#ecebe6,#b5b4ae)}
.spread .headline{position:absolute;left:612px;top:30px;width:40px;height:310px;writing-mode:vertical-rl;transform:rotate(180deg);font-family:"Tinos",serif;font-weight:700;font-size:24px;color:#333;text-align:center}
.spread .edition{position:absolute;left:0;top:0;background:rgba(60,60,60,.78);color:#fff;font-size:34px;line-height:44px;padding:0 6px}
.spread .arrow{position:absolute;top:274px;width:70px;height:70px}

.intro{position:absolute;left:100px;top:878px;width:996px;font-size:22px;line-height:29px}
.intro p{margin-bottom:29px}
.intro h2{font-family:"Gelasio",serif;color:var(--accent-red);font-size:28px;font-weight:400;line-height:34px;margin-top:-4px}
.intro ul{list-style:none;margin:0 0 24px 0}
.intro li{padding-left:100px;position:relative}
.intro li::before{content:"•";position:absolute;left:72px}
.intro .red-link{color:var(--accent-red)}

.rule{position:absolute;left:0;width:1200px;height:2px;background:var(--rule)}

.issues{position:absolute;top:1602px;left:0;width:1200px}
.issues .cover{position:absolute;top:0;width:136px;text-align:center}
.issues .cover .art{height:208px;border:1px solid #888}
.issues .cover .no{font-family:"Tinos",serif;font-size:20px;margin-top:14px;width:220px;margin-left:-42px;line-height:24px}
.issues .cover a{display:block;font-family:"Tinos",serif;font-size:18px;width:220px;margin-left:-42px;line-height:22px}
.issues .tri{position:absolute;top:118px;width:30px;height:60px}
.browse-more{position:absolute;top:1892px;left:0;width:1200px;text-align:center;font-size:22px;font-weight:700}
.browse-more a{color:var(--accent-red)}

.finder h3{position:absolute;font-size:28px;font-weight:400;color:var(--accent-red)}
.finder a{position:absolute;font-size:21px}
.finder .more{color:var(--accent-red);text-decoration:none}

.site-footer{position:absolute;top:2386px;left:0;width:1200px;height:250px;background:var(--footer-dark)}
.site-footer nav a{position:absolute;top:16px;color:#fff;text-decoration:none;font-family:"Tinos",serif;font-size:23px}
.site-footer nav a.current{color:var(--accent-red);text-decoration:underline}
.site-footer .partner{position:absolute;background:#fff}

.licence{position:absolute;left:514px;top:2650px;width:176px;height:60px;background:#1d1d1d;border:3px solid #bbb}
.copyright{position:absolute;top:2716px;left:0;width:1200px;text-align:center;font-family:"Tinos",serif;font-size:14px}
</style>
</head>
<body>

<header>
  <div class="search-bar">
    <div class="field"></div>
    <div class="go"><svg width="40" height="38" viewBox="0 0 40 38"><circle cx="17" cy="16" r="8" fill="none" stroke="#fff" stroke-width="4"/><line x1="23" y1="22" x2="30" y2="29" stroke="#fff" stroke-width="4"/></svg></div>
    <a class="advanced" href="#">Advanced Search</a>
  </div>
  <div class="masthead"><span class="brand">LANTERN WEEKLY</span></div>
  <nav class="main-nav">
    <a class="current" href="#" style="left:198px">Home</a>
    <a href="#" style="left:320px">About</a>
    <a href="#" style="left:442px">Browse Lantern Weekly</a>
    <a href="#" style="left:782px">A-Z People</a>
    <a href="#" style="left:952px">Help</a>
  </nav>
</header>

<section class="spread" aria-label="Featured spread, 1961 edition">
  <div class="panel" role="img" aria-label="Black and white photograph of a wedding party standing on a lawn" style="left:14px;top:20px;width:462px;height:232px;background:linear-gradient(180deg,#5d5d5a,#9c9c96 55%,#c8c8c2)"></div>
  <div class="panel" role="img" aria-label="Block of caption text beneath the wedding photograph" style="left:14px;top:260px;width:462px;height:92px;background:#bdbcb6"></div>
  <div class="panel" role="img" aria-label="Black and white photograph of a second wedding party in front of trees" style="left:14px;top:360px;width:462px;height:254px;background:linear-gradient(180deg,#4a4a47,#8f8f8a 50%,#c4c4be)"></div>
  <div class="gutter"></div>
  <div class="panel" role="img" aria-label="Black and white photograph of a town street with new parking meters" style="left:664px;top:10px;width:302px;height:340px;background:linear-gradient(180deg,#a9a9a4,#7d7d78)"></div>
  <div class="headline">Parking Meters Installed</div>
  <div class="panel" role="img" aria-label="Printed illustration of a traditional carved figure" style="left:506px;top:360px;width:230px;height:254px;background:#c7c6c0"></div>
  <div class="panel" role="img" aria-label="Colour magazine cover with a sunset over water" style="left:738px;top:184px;width:118px;height:222px;margin-top:200px;background:linear-gradient(180deg,#8a6a3c,#2e2a22)"></div>
  <div class="panel" role="img" aria-label="Colour magazine cover with two women seated outdoors" style="left:858px;top:184px;width:118px;height:222px;margin-top:200px;background:linear-gradient(180deg,#c9384d 0 10%,#5f8a6a 10%,#8a6f50)"></div>
  <span class="edition">1961 EDITION</span>
  <svg class="arrow" style="left:4px" viewBox="0 0 70 70"><circle cx="35" cy="35" r="32" fill="#eee" stroke="#333" stroke-width="4"/><path d="M38 22 L24 35 L38 48Z M50 22 L36 35 L50 48Z" fill="#333"/></svg>
  <svg class="arrow" style="left:902px" viewBox="0 0 70 70"><circle cx="35" cy="35" r="32" fill="#eee" stroke="#333" stroke-width="4"/><path d="M32 22 L46 35 L32 48Z M20 22 L34 35 L20 48Z" fill="#333"/></svg>
</section>

<main class="intro">
  <p>Full-text archive of Lantern Weekly, a monthly serial published by Harbour Press Company between 1954 and 1975.</p>
  <p>For two decades residents of Gisborne and East Coast, North Island, New Zealand Aotearoa used to look forward to the latest issue hitting the bookshops.</p>
  <p>Published at a time of rapid social and cultural change, the pictorial serial captured personal and community events through photographs and lively commentary; a snapshot of the care-free heady years from Babyboomers to the first of Generation X.</p>
  <h2>What you can do</h2>
  <div>The website allows you to:</div>
  <ul>
    <li>browse through the entire archive, as well as read complete editions</li>
    <li>search for and read individual articles</li>
    <li>view and print transcripts of articles or images of original journal pages</li>
    <li>search articles by person, title and keyword.</li>
  </ul>
  <h2>Image usage</h2>
  <div>Personal re-use without commercial benefit of images featured on this site is allowed under the <a href="#">Open Share Attribution-NonCommercial-NoDerivs 3.0 New Zealand license</a>. More information is available on our <a class="red-link" href="#">About page</a>.</div>
</main>

<div class="rule" style="top:1554px"></div>

<section class="issues">
  <svg class="tri" style="left:92px" viewBox="0 0 30 60"><path d="M30 0 L0 30 L30 60Z" fill="#111"/></svg>
  <div class="cover" style="left:230px"><div class="art" role="img" aria-label="Cover of issue 77: a child posed in a giant shell" style="background:linear-gradient(180deg,#7d6f72,#b69aa0 60%,#6f6a66)"></div><div class="no">No. 77</div><a href="#">November 3, 1960</a></div>
  <div class="cover" style="left:432px"><div class="art" role="img" aria-label="Cover of issue 82: a swimmer beside a surfboard on the beach" style="background:linear-gradient(180deg,#c7869b,#d8b7b9 55%,#cfc3a4)"></div><div class="no">No. 82</div><a href="#">April 20, 1961</a></div>
  <div class="cover" style="left:634px"><div class="art" role="img" aria-label="Cover of issue 122: a woman in a garden" style="background:linear-gradient(180deg,#4f6e34,#7a5a3a 60%,#3f5a2c)"></div><div class="no">No. 122</div><a href="#">August 13, 1964</a></div>
  <div class="cover" style="left:836px"><div class="art" role="img" aria-label="Cover of issue 126: people in a white convertible by the sea" style="background:linear-gradient(180deg,#5c97cc,#8fb7d6 45%,#d9d9d4 70%,#8a8f7a)"></div><div class="no">No. 126</div><a href="#">December 3, 1964</a></div>
  <svg class="tri" style="left:1080px" viewBox="0 0 30 60"><path d="M0 0 L30 30 L0 60Z" fill="#111"/></svg>
</section>
<div class="browse-more"><a href="#">Browse More Issues</a></div>

<div class="rule" style="top:1944px"></div>

<section class="finder">
  <h3 style="left:218px;top:1988px">Search By Year</h3>
  <a href="#" style="left:218px;top:2050px">1954</a><a href="#" style="left:290px;top:2050px">1955</a><a href="#" style="left:362px;top:2050px">1956</a><a href="#" style="left:434px;top:2050px">1957</a><a href="#" style="left:506px;top:2050px">1958</a>
  <a href="#" style="left:218px;top:2103px">1959</a><a href="#" style="left:290px;top:2103px">1960</a><a href="#" style="left:362px;top:2103px">1961</a><a href="#" style="left:434px;top:2103px">1962</a><a href="#" style="left:506px;top:2103px">1963</a>
  <a href="#" style="left:218px;top:2156px">1964</a><a href="#" style="left:290px;top:2156px">1965</a><a href="#" style="left:362px;top:2156px">1966</a><a href="#" style="left:434px;top:2156px">1967</a><a href="#" style="left:506px;top:2156px">1968</a>
  <a href="#" style="left:218px;top:2209px">1969</a><a href="#" style="left:290px;top:2209px">1970</a><a href="#" style="left:362px;top:2209px">1971</a><a href="#" style="left:434px;top:2209px">1972</a><a href="#" style="left:506px;top:2209px">1973</a>
  <a href="#" style="left:218px;top:2263px">1974</a><a href="#" style="left:290px;top:2263px">1975</a>

  <h3 style="left:630px;top:1988px">Search By Peope / Place</h3>
  <a href="#" style="left:630px;top:2050px">Tom Aldane</a><a href="#" style="left:846px;top:2050px">Jody Ashwin</a>
  <a href="#" style="left:630px;top:2103px">Mark Amberly</a><a href="#" style="left:846px;top:2103px">Paul Arneson</a>
  <a href="#" style="left:630px;top:2156px">Dora Abel</a><a href="#" style="left:846px;top:2156px">Dean Abrey</a>
  <a href="#" style="left:630px;top:2209px">Dan Acton</a><a href="#" style="left:846px;top:2209px">Eliza Acton</a>
  <a href="#" style="left:630px;top:2263px">Keith Acton</a><a href="#" style="left:846px;top:2263px">Simon Acton</a>
  <a class="more" href="#" style="left:888px;top:2314px">More &gt;&gt;</a>
</section>

<footer class="site-footer">
  <nav>
    <a class="current" href="#" style="left:136px">Home</a>
    <a href="#" style="left:248px">About</a>
    <a href="#" style="left:356px">Browse Lantern Weekly</a>
    <a href="#" style="left:690px">A-Z People</a>
    <a href="#" style="left:846px">Help</a>
    <a href="#" style="left:942px">Report an Error</a>
  </nav>
  <div class="partner" style="left:104px;top:76px;width:96px;height:128px"></div>
  <div class="partner" style="left:226px;top:76px;width:108px;height:130px"></div>
  <div class="partner" style="left:362px;top:100px;width:104px;height:108px"></div>
  <div class="partner" style="left:498px;top:128px;width:168px;height:52px"></div>
  <div class="partner" style="left:704px;top:132px;width:186px;height:46px"></div>
  <div class="partner" style="left:908px;top:130px;width:186px;height:48px"></div>
</footer>

<div class="licence" role="img" aria-label="Licence badge"></div>
<div class="copyright">© 2012 Eastbay Memorial Library</div>

</body>
</html>
```